Chewing Gum With Active Ingredients Needs Packaging Design

Brivella Mint Systems is a revolutionary new chewing gum that contains active ingredients commonly found in mouthwashes - it's a portable and convenient way to keep a fresh, clean, and healthy mouth. We have a thorough design brief (attached file) for the packaging we need - a simple sleeve for blister packed gum. We want our design to convey that we are a modern, effective, and high-end product.

Target Market(s)

Young professionals, 20-35 years old

Font styles to use
Serif
Sans Serif

Colors
0292cd
ffffff
0555a3

Requirements
Must have
• A sleek, elegant design
• ALL of the elements listed in the creative brief PDF
• Attached logo
Nice to have
• Incorporation of foil into the design
• A unique, unmistakable look
Should not have
• Too medical of a look

```html
<!DOCTYPE html>
<html lang="en">
<head>
<meta charset="utf-8">
<title>Brivella Mint Systems – Peppermint Sleeve</title>
<link href="https://fonts.googleapis.com/css2?family=Raleway:ital,wght@0,300;0,400;0,600;0,700;1,700&display=swap" rel="stylesheet">
<style>
  :root{
    --navy:#2c2f8a;
    --royal:#0555a3;
    --sky:#0292cd;
    --panel:#1a7bb7;
    --white:#ffffff;
    --quilt-light:#f7f7f7;
    --quilt-shade:#dcdcdc;
    --window:#9cbfa6;
  }
  html,body{margin:0;padding:0;width:1200px;height:1200px;overflow:hidden;background:var(--white);}
  body{font-family:"Raleway",sans-serif;position:relative;}
  .sleeve{position:absolute;left:45px;top:301px;width:1110px;height:597px;}
  .sleeve-shapes{position:absolute;inset:0;}
  .sleeve-text{position:absolute;margin:0;white-space:nowrap;}

  .top-count{left:438px;top:5px;font:italic 700 16px "Raleway",sans-serif;color:var(--white);}
  .top-type{left:530px;top:5px;font:300 16px "Raleway",sans-serif;color:var(--white);}
  .top-flavour{right:56px;top:5px;font:700 15px "Raleway",sans-serif;color:var(--white);}

  .brand-name{left:0;width:1082px;text-align:center;top:160px;font:300 44px "Raleway",sans-serif;color:var(--navy);letter-spacing:0.06em;}
  .brand-sub{left:0;width:1082px;text-align:center;top:207px;font:400 11px "Raleway",sans-serif;color:var(--navy);letter-spacing:0.9em;}

  .count{left:40px;top:468px;color:var(--navy);display:flex;align-items:baseline;gap:2px;}
  .count-num{font:700 48px/1 "Raleway",sans-serif;}
  .count-word{font:700 16px "Raleway",sans-serif;}
  .count-type{left:24px;top:512px;font:300 17px "Raleway",sans-serif;color:var(--navy);}

  .claims{left:918px;top:55px;width:146px;text-align:center;font:300 16px/1.1 "Raleway",sans-serif;color:var(--white);white-space:normal;}
  .flavour{left:932px;top:504px;font:700 26px "Raleway",sans-serif;color:var(--white);}

  .benefits{left:0;width:1110px;top:558px;text-align:center;font:300 17px "Raleway",sans-serif;color:var(--white);word-spacing:1px;}
  .benefits .dot{margin:0 10px;}
</style>
</head>
<body>
  <div class="sleeve">
    <svg class="sleeve-shapes" width="1110" height="597" viewBox="0 0 1110 597" xmlns="http://www.w3.org/2000/svg">
      <defs>
        <linearGradient id="band-top" x1="0" x2="1" y1="0" y2="0">
          <stop offset="0" stop-color="var(--sky)"/>
          <stop offset="0.5" stop-color="var(--navy)"/>
          <stop offset="1" stop-color="var(--royal)"/>
        </linearGradient>
        <linearGradient id="band-bottom" x1="0" x2="1" y1="0" y2="0">
          <stop offset="0" stop-color="var(--navy)"/>
          <stop offset="1" stop-color="var(--sky)"/>
        </linearGradient>
        <linearGradient id="quilt" x1="0" x2="1" y1="0" y2="1">
          <stop offset="0" stop-color="var(--quilt-shade)"/>
          <stop offset="0.5" stop-color="var(--quilt-light)"/>
          <stop offset="1" stop-color="var(--quilt-shade)"/>
        </linearGradient>
      </defs>
      <rect class="quilt-field" x="0" y="30" width="1110" height="515" fill="url(#quilt)" role="img" aria-label="Soft white quilted diamond texture"/>
      <path class="flavour-panel" d="M838 30 L1110 30 L1110 545 L906 545 C880 360 860 180 838 30 Z" fill="var(--panel)"/>
      <path class="panel-edge" d="M838 30 C860 180 880 360 906 545 L896 545 C870 360 850 180 828 30 Z" fill="var(--royal)"/>
      <path class="window" d="M1110 203 L1045 203 Q1028 203 1028 220 L1028 363 Q1028 380 1045 380 L1110 380 Z" fill="var(--window)" stroke="var(--navy)" stroke-width="6" role="img" aria-label="Window showing the gum blister pack"/>
      <rect class="top-band" x="0" y="0" width="1110" height="30" fill="url(#band-top)"/>
      <rect class="bottom-band" x="0" y="543" width="1110" height="54" fill="url(#band-bottom)"/>
      <circle class="brand-mark" cx="541" cy="100" r="44" fill="none" stroke="var(--royal)" stroke-width="5"/>
    </svg>

    <p class="sleeve-text top-count">8 PIECES</p>
    <p class="sleeve-text top-type">SUGAR FREE GUM</p>
    <p class="sleeve-text top-flavour">PEPPERMINT</p>

    <p class="sleeve-text brand-name">BRIVELLA</p>
    <p class="sleeve-text brand-sub">MINT SYSTEMS</p>

    <p class="sleeve-text count"><span class="count-num">8</span><span class="count-word">PIECES</span></p>
    <p class="sleeve-text count-type">SUGAR FREE GUM</p>

    <p class="sleeve-text claims">ASPARTAME FREE WITH XYLITOL</p>
    <p class="sleeve-text flavour">PEPPERMINT</p>

    <p class="sleeve-text benefits">WHITENS TEETH<span class="dot">·</span>FRESHENS BREATH<span class="dot">·</span>HELPS REDUCE PLAQUE<span class="dot">·</span>HELPS PROTECT GUMS</p>
  </div>
</body>
</html>
```